Single-sided business card for restaurant bellwether with new logo made on this site

Business card options with new logo including restaurant name, address, phone number and website. This business card is single-sided only and will be presented at the hostess desk for clients to take. I would like to see options based on a cream card background, a white card background, a yellow card background and a burgundy colored background. It needs to be elegant and traditional.

Target Market(s)

local and international crowd

Industry/Entity Type

restaurant

Contact Information for Business Card

address, website and phone number

Font styles to use
Serif

Colors
EE7325
F08F49
F5BC92
FAE3D3
FDF4ED

Requirements
Must have
• new logo, address, phone number, website
Should not have
• more than three colors

```html
<!DOCTYPE html>
<html lang="es">
<head>
<meta charset="utf-8">
<title>Bellwether – Tarjeta de presentación</title>
<link href="https://fonts.googleapis.com/css2?family=Montserrat:wght@400;500&display=swap" rel="stylesheet">
<style>
  :root {
    --page-bg: #2a2a2a;
    --card-cream: #fdefd3;
    --ink-dark: #3b1b1d;
    --ink-text: #4a2b2b;
  }
  * { margin: 0; padding: 0; box-sizing: border-box; }
  html, body {
    width: 1200px;
    height: 800px;
    overflow: hidden;
    background: var(--page-bg);
  }
  .canvas {
    width: 1200px;
    height: 800px;
    display: flex;
    align-items: center;
    justify-content: center;
  }
  .business-card {
    position: relative;
    width: 1000px;
    height: 566px;
    background: var(--card-cream);
    font-family: "Montserrat", sans-serif;
    color: var(--ink-text);
  }
  .card-frame {
    position: absolute;
    inset: 27px 28px 28px 28px;
    border: 3px solid var(--ink-dark);
  }
  .brand-block {
    position: absolute;
    left: 200px;
    top: 172px;
    width: 208px;
    display: flex;
    flex-direction: column;
    align-items: center;
  }
  .brand-square {
    width: 122px;
    height: 122px;
    background: var(--ink-dark);
  }
  .brand-name {
    margin-top: 34px;
    font-family: "Montserrat", sans-serif;
    font-weight: 500;
    font-size: 27px;
    letter-spacing: 4px;
    color: var(--ink-dark);
    text-transform: uppercase;
  }
  .divider {
    position: absolute;
    left: 451px;
    top: 150px;
    width: 2px;
    height: 250px;
    background: var(--ink-dark);
  }
  .contact-block {
    position: absolute;
    left: 488px;
    top: 168px;
    font-weight: 400;
  }
  .address {
    font-style: normal;
    font-size: 22px;
    line-height: 28px;
    letter-spacing: 0.3px;
  }
  .reservations-label {
    margin-top: 10px;
    font-size: 21px;
    letter-spacing: 0.3px;
  }
  .phone {
    margin-top: 4px;
    font-size: 29px;
    letter-spacing: 0.2px;
  }
  .website {
    margin-top: 12px;
    font-size: 21px;
    letter-spacing: 0.8px;
  }
</style>
</head>
<body>
<main class="canvas">
  <article class="business-card">
    <div class="card-frame"></div>

    <div class="brand-block">
      <div class="brand-square"></div>
      <div class="brand-name">Bellwether</div>
    </div>

    <div class="divider"></div>

    <section class="contact-block">
      <address class="address">
        Restaurant Bellwether<br>
        Calle Jacaranda 415<br>
        Bahía del Sol<br>
        Oaxaca CP 70312
      </address>
      <p class="reservations-label">Reservaciones</p>
      <p class="phone">958-214-3370</p>
      <p class="website">www.bellwether.com.mx</p>
    </section>
  </article>
</main>
</body>
</html>
```